Audio Spectrum Infographic

We need an infographic similar to the attached for an online course. There are a few changes but we are generally looking for better colors and a less cluttered design with more clarity.

For the types (Vocals -Harp) we would like to include as many as possible without the clutter. Better fonts and non-distracting background colors will help.

The Sound Effects section (Rumble, Tinny, etc) needs to stay but perhaps more buttons and less lines. We would like it to be easy to read and less cluttered.

The "DKV 1/3rd octave Equalizer Bands" and wave image can be removed.

The Sub Bass, Bass, Midrange, High Mids, High Frequency information needs to stay.

We will have other graphics to complete once this is completed.

```html
<!DOCTYPE html>
<html lang="en">
<head>
<meta charset="utf-8">
<title>Audio Spectrum Infographic</title>
<link rel="stylesheet" href="https://fonts.googleapis.com/css2?family=Roboto:wght@400;500;700&family=Roboto+Condensed:wght@400;700&display=swap">
<style>
  :root {
    --bg-top: #2a2d32;
    --bg-bottom: #1b1d21;
    --bar-strip: #131518;
    --side-col: #202226;
    --grid: rgba(255,255,255,0.09);
    --grid-band: rgba(255,255,255,0.22);
    --text: #f4f5f7;
    --text-dim: #cfd3d8;
    --cool-start: #27d6f0;
    --cool-end: #3f6ce6;
    --warm-start: #f2774e;
    --warm-mid: #f6b23c;
    --warm-end: #f4dc40;
    --overtone: #ffffff;
    --keys-light: #f2f2f2;
    --keys-shade: #c9c9c9;
    --pill-start: #28d4ef;
    --pill-end: #3a74e6;
    --marker: #35c8f0;
  }
  html, body { margin: 0; padding: 0; width: 1200px; height: 943px; overflow: hidden; background: var(--bg-bottom); }
  .spectrum { display: block; width: 1200px; height: 943px; font-family: "Roboto", Arial, sans-serif; }
  .axis-label { fill: var(--text-dim); font-size: 11px; text-anchor: middle; }
  .axis-unit { fill: var(--text-dim); font-size: 11px; }
  .section-label { fill: var(--text); font-family: "Roboto Condensed", Arial, sans-serif; font-weight: 700; font-size: 12px; text-anchor: middle; }
  .instrument-label { fill: var(--text); font-family: "Roboto Condensed", Arial, sans-serif; font-weight: 700; font-size: 12.5px; text-anchor: end; }
  .instrument-label.after { text-anchor: start; }
  .seg-cool { fill: url(#coolGrad); }
  .seg-warm { fill: url(#warmGrad); }
  .seg-overtone { fill: var(--overtone); }
  .grid-line { stroke: var(--grid); stroke-width: 1; }
  .band-line { stroke: var(--grid-band); stroke-width: 1; stroke-dasharray: 4 4; }
  .section-divider { stroke: rgba(255,255,255,0.14); stroke-width: 1; }
  .piano-title { fill: var(--text); font-family: "Roboto Condensed", Arial, sans-serif; font-weight: 700; font-size: 12px; text-anchor: middle; }
  .piano-bracket { stroke: var(--marker); stroke-width: 1; fill: none; }
  .keyboard-area { fill: url(#keysGrad); }
  .marker-line { stroke: var(--marker); stroke-width: 2; }
  .marker-label { fill: var(--text); font-size: 11px; text-anchor: middle; }
  .pill { fill: url(#pillGrad); }
  .pill-text { fill: #fff; font-size: 11px; text-anchor: middle; font-weight: 500; }
  .pill-text.small { font-size: 8px; }
  .band-name { fill: var(--text); font-family: "Roboto Condensed", Arial, sans-serif; font-weight: 700; font-size: 13px; text-anchor: middle; }
</style>
</head>
<body>
<svg class="spectrum" viewBox="0 0 993 780" width="1200" height="943" xmlns="http://www.w3.org/2000/svg">
  <defs>
    <linearGradient id="pageGrad" x1="0" y1="0" x2="0" y2="1">
      <stop offset="0" style="stop-color:var(--bg-top)"/>
      <stop offset="1" style="stop-color:var(--bg-bottom)"/>
    </linearGradient>
    <linearGradient id="coolGrad" x1="0" y1="0" x2="1" y2="0">
      <stop offset="0" style="stop-color:var(--cool-start)"/>
      <stop offset="1" style="stop-color:var(--cool-end)"/>
    </linearGradient>
    <linearGradient id="warmGrad" x1="0" y1="0" x2="1" y2="0">
      <stop offset="0" style="stop-color:var(--warm-start)"/>
      <stop offset="0.5" style="stop-color:var(--warm-mid)"/>
      <stop offset="1" style="stop-color:var(--warm-end)"/>
    </linearGradient>
    <linearGradient id="pillGrad" x1="0" y1="0" x2="1" y2="0">
      <stop offset="0" style="stop-color:var(--pill-start)"/>
      <stop offset="1" style="stop-color:var(--pill-end)"/>
    </linearGradient>
    <linearGradient id="keysGrad" x1="0" y1="0" x2="0" y2="1">
      <stop offset="0" style="stop-color:var(--keys-light)"/>
      <stop offset="1" style="stop-color:var(--keys-shade)"/>
    </linearGradient>
  </defs>

  <rect width="993" height="780" fill="url(#pageGrad)"/>
  <rect x="0" y="28" width="30" height="490" fill="var(--side-col)"/>

  <g class="grid">
    <line class="grid-line" x1="66" y1="28" x2="66" y2="520"/>
    <line class="grid-line" x1="165" y1="28" x2="165" y2="520"/>
    <line class="grid-line" x1="283" y1="28" x2="283" y2="520"/>
    <line class="grid-line" x1="360" y1="28" x2="360" y2="520"/>
    <line class="grid-line" x1="467" y1="28" x2="467" y2="520"/>
    <line class="grid-line" x1="517" y1="28" x2="517" y2="520"/>
    <line class="grid-line" x1="586" y1="28" x2="586" y2="520"/>
    <line class="grid-line" x1="767" y1="28" x2="767" y2="520"/>
    <line class="grid-line" x1="882" y1="28" x2="882" y2="520"/>
    <line class="grid-line" x1="941" y1="28" x2="941" y2="520"/>
    <line class="band-line" x1="218" y1="28" x2="218" y2="725"/>
    <line class="band-line" x1="402" y1="28" x2="402" y2="725"/>
    <line class="band-line" x1="675" y1="28" x2="675" y2="725"/>
    <line class="band-line" x1="808" y1="28" x2="808" y2="725"/>
  </g>

  <rect x="0" y="0" width="993" height="28" fill="var(--bar-strip)"/>
  <g class="axis-top">
    <text class="axis-unit" x="8" y="19">Hz</text>
    <text class="axis-label" x="66" y="19">20</text>
    <text class="axis-label" x="165" y="19">40</text>
    <text class="axis-label" x="212" y="19">60</text>
    <text class="axis-label" x="283" y="19">100</text>
    <text class="axis-label" x="360" y="19">200</text>
    <text class="axis-label" x="467" y="19">400</text>
    <text class="axis-label" x="517" y="19">600</text>
    <text class="axis-label" x="586" y="19">1K</text>
    <text class="axis-label" x="679" y="19">2K</text>
    <text class="axis-label" x="767" y="19">4K</text>
    <text class="axis-label" x="818" y="19">6K</text>
    <text class="axis-label" x="882" y="19">10K</text>
    <text class="axis-label" x="941" y="19">16K</text>
    <text class="axis-label" x="973" y="19">20K</text>
  </g>

  <g class="sections">
    <text class="section-label" transform="translate(19 53) rotate(90)">Vocal</text>
    <text class="section-label" transform="translate(19 127) rotate(90)">Percussion</text>
    <text class="section-label" transform="translate(19 221) rotate(90)">Brass</text>
    <text class="section-label" transform="translate(19 331) rotate(90)">Woodwinds</text>
    <text class="section-label" transform="translate(19 457) rotate(90)">Strings</text>
    <line class="section-divider" x1="0" y1="77" x2="993" y2="77"/>
    <line class="section-divider" x1="0" y1="177" x2="993" y2="177"/>
    <line class="section-divider" x1="0" y1="265" x2="993" y2="265"/>
    <line class="section-divider" x1="0" y1="397" x2="993" y2="397"/>
    <line class="section-divider" x1="0" y1="518" x2="993" y2="518"/>
  </g>

  <g class="ranges">
    <g class="instrument"><text class="instrument-label" x="278" y="49">Male</text>
      <rect class="seg-cool" x="285" y="43" width="285" height="4" rx="2"/><rect class="seg-warm" x="570" y="43" width="290" height="4"/><rect class="seg-overtone" x="860" y="43" width="85" height="4" rx="2"/></g>
    <g class="instrument"><text class="instrument-label" x="393" y="65">Female</text>
      <rect class="seg-cool" x="400" y="59" width="190" height="4" rx="2"/><rect class="seg-warm" x="590" y="59" width="270" height="4"/><rect class="seg-overtone" x="860" y="59" width="85" height="4" rx="2"/></g>

    <g class="instrument"><text class="instrument-label" x="144" y="91">Kick</text>
      <rect class="seg-cool" x="193" y="85" width="297" height="4" rx="2"/><rect class="seg-warm" x="490" y="85" width="362" height="4" rx="2"/></g>
    <g class="instrument"><text class="instrument-label" x="196" y="107">Tympany</text>
      <rect class="seg-cool" x="218" y="101" width="312" height="4" rx="2"/><rect class="seg-warm" x="530" y="101" width="198" height="4" rx="2"/></g>
    <g class="instrument"><text class="instrument-label" x="225" y="122">Toms</text>
      <rect class="seg-cool" x="236" y="116" width="254" height="4" rx="2"/><rect class="seg-warm" x="490" y="116" width="352" height="4" rx="2"/></g>
    <g class="instrument"><text class="instrument-label" x="257" y="137">Snare</text>
      <rect class="seg-cool" x="283" y="131" width="117" height="4" rx="2"/><rect class="seg-warm" x="400" y="131" width="482" height="4" rx="2"/></g>
    <g class="instrument"><text class="instrument-label" x="299" y="153">Congas</text>
      <rect class="seg-cool" x="335" y="147" width="245" height="4" rx="2"/><rect class="seg-warm" x="580" y="147" width="217" height="4" rx="2"/></g>
    <g class="instrument"><text class="instrument-label" x="348" y="168">Cymbals</text>
      <rect class="seg-overtone" x="355" y="162" width="72" height="4" rx="2"/><rect class="seg-cool" x="427" y="162" width="143" height="4"/><rect class="seg-warm" x="570" y="162" width="367" height="4" rx="2"/></g>

    <g class="instrument"><text class="instrument-label" x="76" y="194">Tuba</text>
      <rect class="seg-overtone" x="122" y="188" width="54" height="4" rx="2"/><rect class="seg-cool" x="176" y="188" width="277" height="4"/><rect class="seg-warm" x="453" y="188" width="225" height="4" rx="2"/></g>
    <g class="instrument"><text class="instrument-label" x="144" y="209">French Horn</text>
      <rect class="seg-overtone" x="210" y="203" width="23" height="4" rx="2"/><rect class="seg-cool" x="233" y="203" width="324" height="4"/><rect class="seg-warm" x="557" y="203" width="240" height="4" rx="2"/></g>
    <g class="instrument"><text class="instrument-label" x="200" y="224">Bass Trombone</text>
      <rect class="seg-cool" x="213" y="218" width="250" height="4" rx="2"/><rect class="seg-warm" x="463" y="218" width="332" height="4"/><rect class="seg-overtone" x="795" y="218" width="83" height="4" rx="2"/></g>
    <g class="instrument"><text class="instrument-label" x="256" y="240">Tenor Trombone</text>
      <rect class="seg-cool" x="258" y="234" width="239" height="4" rx="2"/><rect class="seg-warm" x="497" y="234" width="303" height="4"/><rect class="seg-overtone" x="800" y="234" width="73" height="4" rx="2"/></g>
    <g class="instrument"><text class="instrument-label" x="329" y="255">Trumpet</text>
      <rect class="seg-cool" x="343" y="249" width="265" height="4" rx="2"/><rect class="seg-warm" x="608" y="249" width="265" height="4" rx="2"/></g>

    <g class="instrument"><text class="instrument-label after" x="785" y="281">Contrabassoon</text>
      <rect class="seg-cool" x="101" y="275" width="262" height="4" rx="2"/><rect class="seg-warm" x="363" y="275" width="400" height="4" rx="2"/></g>
    <g class="instrument"><text class="instrument-label" x="166" y="297">Bassoon</text>
      <rect class="seg-cool" x="208" y="291" width="317" height="4" rx="2"/><rect class="seg-warm" x="525" y="291" width="347" height="4" rx="2"/></g>
    <g class="instrument"><text class="instrument-label" x="222" y="312">Tenor Sax</text>
      <rect class="seg-cool" x="300" y="306" width="237" height="4" rx="2"/><rect class="seg-warm" x="537" y="306" width="323" height="4"/><rect class="seg-overtone" x="860" y="306" width="65" height="4" rx="2"/></g>
    <g class="instrument"><text class="instrument-label" x="267" y="327">Alto Sax</text>
      <rect class="seg-cool" x="316" y="321" width="229" height="4" rx="2"/><rect class="seg-warm" x="545" y="321" width="315" height="4"/><rect class="seg-overtone" x="860" y="321" width="65" height="4" rx="2"/></g>
    <g class="instrument"><text class="instrument-label" x="309" y="343">Clarinet</text>
      <rect class="seg-cool" x="316" y="337" width="365" height="4" rx="2"/><rect class="seg-warm" x="681" y="337" width="233" height="4" rx="2"/></g>
    <g class="instrument"><text class="instrument-label" x="355" y="358">Oboe</text>
      <rect class="seg-cool" x="387" y="352" width="263" height="4" rx="2"/><rect class="seg-warm" x="650" y="352" width="264" height="4" rx="2"/></g>
    <g class="instrument"><text class="instrument-label" x="388" y="373">Flute</text>
      <rect class="seg-cool" x="402" y="367" width="284" height="4" rx="2"/><rect class="seg-warm" x="686" y="367" width="217" height="4" rx="2"/></g>
    <g class="instrument"><text class="instrument-label" x="492" y="389">Piccolo</text>
      <rect class="seg-cool" x="519" y="383" width="242" height="4" rx="2"/><rect class="seg-warm" x="761" y="383" width="160" height="4" rx="2"/></g>

    <g class="instrument"><text class="instrument-label" x="106" y="414">Bass</text>
      <rect class="seg-overtone" x="121" y="408" width="41" height="4" rx="2"/><rect class="seg-cool" x="162" y="408" width="281" height="4"/><rect class="seg-warm" x="443" y="408" width="354" height="4" rx="2"/></g>
    <g class="instrument"><text class="instrument-label" x="210" y="430">Cello</text>
      <rect class="seg-cool" x="224" y="424" width="273" height="4" rx="2"/><rect class="seg-warm" x="497" y="424" width="351" height="4" rx="2"/></g>
    <g class="instrument"><text class="instrument-label" x="296" y="445">Viola</text>
      <rect class="seg-cool" x="312" y="439" width="269" height="4" rx="2"/><rect class="seg-warm" x="581" y="439" width="247" height="4" rx="2"/></g>
    <g class="instrument"><text class="instrument-label" x="356" y="461">Violin</text>
      <rect class="seg-cool" x="368" y="455" width="250" height="4" rx="2"/><rect class="seg-warm" x="618" y="455" width="319" height="4" rx="2"/></g>
    <g class="instrument"><text class="instrument-label" x="243" y="476">Guitar</text>
      <rect class="seg-cool" x="255" y="470" width="351" height="4" rx="2"/><rect class="seg-warm" x="606" y="470" width="189" height="4" rx="2"/></g>
    <g class="instrument"><text class="instrument-label" x="99" y="492">Harp</text>
      <rect class="seg-cool" x="113" y="486" width="620" height="4" rx="2"/><rect class="seg-warm" x="733" y="486" width="83" height="4" rx="2"/></g>
    <g class="instrument"><text class="instrument-label after" x="868" y="507">Pipe Organ</text>
      <rect class="seg-cool" x="65" y="501" width="785" height="4" rx="2"/></g>
  </g>

  <g class="piano">
    <text class="piano-title" x="429" y="538">Standard 88-key Piano</text>
    <path class="piano-bracket" d="M100 552 V545 H778 V552"/>
    <rect class="keyboard-area" x="37" y="553" width="905" height="39" role="img" aria-label="Piano keyboard spanning octaves 0 to 9, aligned to the frequency scale"/>
    <line class="marker-line" x1="408" y1="592" x2="408" y2="603"/>
    <text class="marker-label" x="410" y="618">Middle C</text>
    <line class="marker-line" x1="479" y1="592" x2="479" y2="603"/>
    <text class="marker-label" x="479" y="614">A</text>
    <text class="marker-label" x="479" y="627">440</text>
  </g>

  <g class="tags">
    <rect class="pill" x="104" y="601" width="58" height="17" rx="5"/><text class="pill-text" x="133" y="613">Rumble</text>
    <rect class="pill" x="64" y="629" width="84" height="17" rx="5"/><text class="pill-text" x="106" y="641">Chest/Thump</text>
    <rect class="pill" x="220" y="622" width="44" height="16" rx="5"/><text class="pill-text small" x="242" y="633">Bottom</text>
    <rect class="pill" x="190" y="650" width="44" height="15" rx="5"/><text class="pill-text small" x="212" y="660">AC/Ground</text>
    <rect class="pill" x="282" y="666" width="72" height="17" rx="5"/><text class="pill-text" x="318" y="678">Boom/Punch</text>
    <rect class="pill" x="322" y="638" width="68" height="17" rx="5"/><text class="pill-text" x="356" y="650">Warmth</text>
    <rect class="pill" x="395" y="654" width="84" height="18" rx="5"/><text class="pill-text" x="437" y="667">Fullness/Mud</text>
    <rect class="pill" x="478" y="635" width="92" height="18" rx="5"/><text class="pill-text" x="524" y="648">Honk</text>
    <rect class="pill" x="550" y="610" width="100" height="18" rx="5"/><text class="pill-text" x="600" y="623">Whack</text>
    <rect class="pill" x="584" y="655" width="92" height="18" rx="5"/><text class="pill-text" x="630" y="668">Tinny</text>
    <rect class="pill" x="670" y="621" width="86" height="18" rx="5"/><text class="pill-text" x="713" y="634">Crunch</text>
    <rect class="pill" x="766" y="598" width="110" height="18" rx="5"/><text class="pill-text" x="821" y="611">Sibilance</text>
    <rect class="pill" x="812" y="625" width="68" height="16" rx="5"/><text class="pill-text" x="846" y="637">Definition</text>
    <rect class="pill" x="745" y="643" width="58" height="18" rx="5"/><text class="pill-text" x="774" y="656">Edge</text>
    <rect class="pill" x="865" y="652" width="42" height="16" rx="5"/><text class="pill-text" x="886" y="664">Pierce</text>
    <rect class="pill" x="928" y="610" width="46" height="18" rx="5"/><text class="pill-text" x="951" y="623">Air</text>
    <rect class="pill" x="677" y="678" width="297" height="18" rx="5"/><text class="pill-text" x="825" y="691">Treble</text>
  </g>

  <g class="axis-third">
    <text class="axis-label" x="65" y="716">20</text>
    <text class="axis-label" x="97" y="716">25</text>
    <text class="axis-label" x="124" y="716">31.5</text>
    <text class="axis-label" x="163" y="716">40</text>
    <text class="axis-label" x="193" y="716">50</text>
    <text class="axis-label" x="236" y="716">63</text>
    <text class="axis-label" x="257" y="716">80</text>
    <text class="axis-label" x="283" y="716">100</text>
    <text class="axis-label" x="312" y="716">125</text>
    <text class="axis-label" x="338" y="716">160</text>
    <text class="axis-label" x="365" y="716">200</text>
    <text class="axis-label" x="397" y="716">250</text>
    <text class="axis-label" x="424" y="716">315</text>
    <text class="axis-label" x="463" y="716">400</text>
    <text class="axis-label" x="492" y="716">500</text>
    <text class="axis-label" x="528" y="716">630</text>
    <text class="axis-label" x="558" y="716">800</text>
    <text class="axis-label" x="582" y="716">1K</text>
    <text class="axis-label" x="613" y="716">1.25K</text>
    <text class="axis-label" x="645" y="716">1.6K</text>
    <text class="axis-label" x="676" y="716">2K</text>
    <text class="axis-label" x="703" y="716">2.5K</text>
    <text class="axis-label" x="735" y="716">3.15K</text>
    <text class="axis-label" x="762" y="716">4K</text>
    <text class="axis-label" x="792" y="716">5K</text>
    <text class="axis-label" x="827" y="716">6.3K</text>
    <text class="axis-label" x="852" y="716">8K</text>
    <text class="axis-label" x="885" y="716">10K</text>
    <text class="axis-label" x="913" y="716">12.5K</text>
    <text class="axis-label" x="942" y="716">16K</text>
    <text class="axis-label" x="971" y="716">20K</text>
  </g>

  <line x1="0" y1="725" x2="993" y2="725" stroke="rgba(255,255,255,0.25)"/>
  <g class="bands">
    <text class="band-name" x="127" y="745">Sub Bass</text>
    <text class="band-name" x="309" y="746">Bass</text>
    <text class="band-name" x="539" y="746">Mid Range</text>
    <text class="band-name" x="746" y="744">High Mids</text>
    <text class="band-name" x="904" y="746">High Freqs</text>
  </g>

  <rect x="0" y="755" width="993" height="25" fill="var(--bar-strip)"/>
  <g class="axis-bottom">
    <text class="axis-unit" x="8" y="772">Hz</text>
    <text class="axis-label" x="66" y="772">20</text>
    <text class="axis-label" x="165" y="772">40</text>
    <text class="axis-label" x="212" y="772">60</text>
    <text class="axis-label" x="360" y="772">200</text>
    <text class="axis-label" x="467" y="772">400</text>
    <text class="axis-label" x="517" y="772">600</text>
    <text class="axis-label" x="586" y="772">1K</text>
    <text class="axis-label" x="679" y="772">2K</text>
    <text class="axis-label" x="767" y="772">4K</text>
    <text class="axis-label" x="818" y="772">6K</text>
    <text class="axis-label" x="882" y="772">10K</text>
    <text class="axis-label" x="941" y="772">16K</text>
    <text class="axis-label" x="973" y="772">20K</text>
  </g>
</svg>
</body>
</html>
```